Business Card Design needed for logo design project

Our business needs a business card design. I'm not sure what format files are generally delivered back, but clearly I will need the ability to edit to add colleagues contact details.

Our logo is attached.

Brivanor is a 3D design services company, providing app, serious/educational game, VR and AR websites/applications to corporate clients.

Target Market(s)

Corporate blue-chip clients needing 3D design services

Industry/Entity Type

Business

Font styles to use
Sans Serif

Requirements
Must have
• Templated such that I can add details (name, phone number etc). Needs to include logo from previous project winner - attached.

```html
<!DOCTYPE html>
<html lang="en">
<head>
<meta charset="utf-8">
<title>Brivanor Business Card</title>
<link href="https://fonts.googleapis.com/css2?family=Lato:wght@300;400;700&display=swap" rel="stylesheet">
<style>
  :root {
    --bg: #ece9e4;
    --card: #f7f7f7;
    --card-edge: #e2e2e2;
    --red: #e52c35;
    --charcoal: #3f3f43;
    --text: #333336;
    --muted: #55555a;
  }
  * { margin: 0; padding: 0; box-sizing: border-box; }
  html, body { width: 1200px; height: 675px; overflow: hidden; }
  body {
    background: var(--bg);
    font-family: "Lato", sans-serif;
    position: relative;
  }
  .card {
    position: absolute;
    top: 182px;
    width: 520px;
    height: 310px;
    background: linear-gradient(160deg, #fbfbfb 0%, var(--card) 55%, #efefef 100%);
    border: 1px solid var(--card-edge);
    box-shadow: 0 10px 24px rgba(0,0,0,0.12);
    overflow: hidden;
  }
  .card-front { left: 55px; }
  .card-back { left: 625px; }

  .brand {
    position: absolute;
    display: flex;
    align-items: center;
    gap: 14px;
  }
  .brand-dot {
    width: 40px; height: 40px;
    border-radius: 50%;
    background: var(--red);
    flex: none;
  }
  .brand-name {
    font-weight: 300;
    font-size: 34px;
    letter-spacing: 4px;
    color: var(--text);
    text-transform: uppercase;
  }
  .card-front .brand { left: 30px; top: 160px; }

  .divider-line {
    position: absolute;
    left: 300px; top: 40px;
    width: 1px; height: 100px;
    background: var(--red);
    transform: rotate(42deg);
    transform-origin: center;
    opacity: 0.8;
  }

  .holder {
    position: absolute;
    right: 28px; top: 26px;
    text-align: right;
    text-transform: uppercase;
  }
  .holder-company { color: var(--red); font-size: 19px; font-weight: 400; letter-spacing: 0.5px; }
  .holder-role { color: var(--muted); font-size: 15px; letter-spacing: 0.5px; }

  .contacts {
    position: absolute;
    right: 28px; top: 112px;
    list-style: none;
    font-size: 11.5px;
    color: var(--text);
    letter-spacing: 0.3px;
  }
  .contacts li {
    display: flex;
    justify-content: flex-end;
    align-items: center;
    gap: 8px;
    height: 19px;
  }
  .contacts svg { width: 11px; height: 11px; flex: none; }

  .edge-band { position: absolute; left: 0; bottom: 0; width: 520px; height: 70px; }

  .card-back .brand {
    left: 50%; top: 50%;
    transform: translate(-50%, -50%);
    gap: 16px;
  }
  .card-back .brand-dot { width: 50px; height: 50px; }
  .card-back .brand-name { font-size: 40px; letter-spacing: 5px; }
</style>
</head>
<body>
  <section class="card card-front" aria-label="Business card front">
    <div class="brand">
      <span class="brand-dot"></span>
      <span class="brand-name">Brivanor</span>
    </div>

    <span class="divider-line"></span>

    <div class="holder">
      <p class="holder-company">Company Name</p>
      <p class="holder-role">Director</p>
    </div>

    <ul class="contacts">
      <li>+44 20 7946 0181
        <svg viewBox="0 0 12 12"><path fill="var(--red)" d="M2.5 1l2 2.2-1 1.2a6 6 0 0 0 3.8 3.8l1.2-1 2.2 2-1.2 1.6C5.5 10.8 1.2 6.5 1 2.2z"/></svg>
      </li>
      <li>+44 20 7946 0182
        <svg viewBox="0 0 12 12"><rect x="1.5" y="2" width="9" height="8" rx="1" fill="none" stroke="var(--red)" stroke-width="1.4"/><rect x="3.5" y="4" width="5" height="2" fill="var(--red)"/></svg>
      </li>
      <li>HELLO@BRIVANOR.COM
        <svg viewBox="0 0 12 12"><circle cx="6" cy="6" r="5.5" fill="var(--red)"/><rect x="3" y="4" width="6" height="4" fill="none" stroke="#fff" stroke-width="0.9"/><path d="M3 4l3 2.2L9 4" fill="none" stroke="#fff" stroke-width="0.9"/></svg>
      </li>
      <li>WWW.BRIVANOR.COM
        <svg viewBox="0 0 12 12"><circle cx="6" cy="6" r="5.5" fill="var(--red)"/><circle cx="6" cy="6" r="3" fill="none" stroke="#fff" stroke-width="0.9"/><path d="M3 6h6M6 3v6" stroke="#fff" stroke-width="0.9"/></svg>
      </li>
    </ul>

    <svg class="edge-band" viewBox="0 0 520 70" aria-hidden="true">
      <path d="M0 44 H220 L234 30 H520 V36 H236 L222 50 H0 Z" fill="var(--charcoal)"/>
      <path d="M0 54 H224 L238 40 H520 V70 H0 Z" fill="var(--red)"/>
    </svg>
  </section>

  <section class="card card-back" aria-label="Business card back">
    <div class="brand">
      <span class="brand-dot"></span>
      <span class="brand-name">Brivanor</span>
    </div>
  </section>
</body>
</html>
```